Postcard Designs - Brantley and Corvane

We are a locally owned, family operated pool service and repair company. The postcards we want to have designed is to co-market with two different companies (Brantley and Corvane) . Both companies manufacture variable speed pumps. We are looking for customers who want to upgrade their systems to save $ on energy costs.

Both postcards are basically the same (and can use the same image rather than 2 different like I have in the Word doc). We just need to modify the text and company logo.

Postcard Specs

Full Bleed Size (starting document size)
8.64" x 5.59"
219 x 142 mm
2592 x 1677 pixels
* Finished artwork should use the full bleed dimensions for best results.
Document Trim Size (final size after being cut)
8.52" x 5.47"
216 x 139 mm
2556 x 1642 pixels
* Please be sure to keep all text within the safe margin.
Resolution
300 DPI

Target Market(s)

Adults in Northern California ages 30 - 80 that make the buying decisions for their families.

Industry/Entity Type

Pool Service

Font styles to use
Sans Serif

Colors
33a6d7
3277b5
acd037
fece3e

Requirements
Must have
• - company logo
- detail on variable speed pump
- cost savings chart
- image of family having fun (something related to the question on the front of the postcard - what would you do with $100/month?)

```html
<!DOCTYPE html>
<html lang="en">
<head>
<meta charset="utf-8">
<title>Brantley Variable Speed Pumps Postcard</title>
<link rel="stylesheet" href="https://fonts.googleapis.com/css2?family=Source+Sans+3:ital,wght@0,400;0,600;0,700;1,600&display=swap">
<style>
  :root {
    --sky-blue: #33a6d7;
    --deep-blue: #3277b5;
    --brand-blue: #1f6fb8;
    --white: #ffffff;
    --backdrop: #e9e9e9;
    --photo-sky-top: #5f8fc4;
    --photo-sky-low: #b9d3ea;
    --photo-sea: #8fd3d6;
    --photo-shore: #d9efe9;
    --photo-sand: #eee6da;
  }
  * { margin: 0; padding: 0; box-sizing: border-box; }
  html, body {
    width: 1200px;
    height: 878px;
    overflow: hidden;
    background: var(--backdrop);
    font-family: "Source Sans 3", sans-serif;
  }
  .postcard {
    position: absolute;
    left: 83px;
    top: 104px;
    width: 1033px;
    height: 670px;
    display: flex;
    background: var(--white);
  }
  .family-photo {
    width: 661px;
    height: 100%;
    background: linear-gradient(to bottom,
      var(--photo-sky-top) 0%,
      var(--photo-sky-low) 60%,
      var(--photo-sea) 63%,
      var(--photo-shore) 88%,
      var(--photo-sand) 91%,
      var(--photo-sand) 100%);
  }
  .offer-panel {
    position: relative;
    width: 372px;
    height: 100%;
  }
  .offer-waves {
    position: absolute;
    inset: 0;
    width: 372px;
    height: 547px;
    display: block;
  }
  .offer-headline {
    position: absolute;
    top: 24px;
    right: 29px;
    text-align: right;
    color: var(--white);
    font-style: italic;
    font-weight: 600;
    font-size: 33px;
    line-height: 48px;
  }
  .offer-detail {
    position: absolute;
    top: 296px;
    left: 17px;
    width: 325px;
    color: var(--white);
    font-weight: 400;
    font-size: 25px;
    line-height: 34px;
    text-align: justify;
  }
  .brand-footer {
    position: absolute;
    left: 0;
    top: 547px;
    width: 372px;
    height: 123px;
    background: var(--white);
    display: flex;
    align-items: center;
    padding-left: 20px;
  }
  .brand-mark {
    width: 50px;
    height: 50px;
    background: var(--brand-blue);
    flex: none;
    margin-right: 12px;
  }
  .brand-lockup {
    display: flex;
    flex-direction: column;
    align-items: flex-end;
  }
  .brand-name {
    color: var(--brand-blue);
    font-weight: 700;
    font-size: 50px;
    line-height: 46px;
    letter-spacing: 0.5px;
  }
  .brand-tagline {
    color: var(--brand-blue);
    font-weight: 700;
    font-size: 17px;
    line-height: 20px;
  }
</style>
</head>
<body>
  <main class="postcard">
    <div class="family-photo" role="img" aria-label="Family of four holding hands on a sandy beach, looking out at the sea under a blue sky"></div>

    <section class="offer-panel">
      <svg class="offer-waves" viewBox="0 0 372 547" aria-hidden="true">
        <rect width="372" height="547" fill="var(--sky-blue)"/>
        <path d="M0,197 C60,180 120,174 190,188 C260,203 320,245 372,252 L372,547 L0,547 Z" fill="var(--deep-blue)"/>
        <path d="M0,197 C60,180 120,174 190,188 C260,203 320,245 372,252" fill="none" stroke="var(--white)" stroke-width="2"/>
      </svg>

      <h1 class="offer-headline">What would<br>you do with…<br>…$50-$100/month?</h1>

      <p class="offer-detail">Moving to a variable speed pump saves an average of $50 - $100/month on your energy bill.</p>

      <div class="brand-footer">
        <div class="brand-mark"></div>
        <div class="brand-lockup">
          <span class="brand-name">BRANTLEY</span>
          <span class="brand-tagline">Variable Speed Pumps</span>
        </div>
      </div>
    </section>
  </main>
</body>
</html>
```